Harbor Healthcare Coming Soon Sign

I need a large (10 x5) road banner announcing the construction of our new medical practice at 5817 Marlow Creek Road in John's Island. The name of our practice is Harbor Healthcare and we thought it would be fund to nick name it the "Harbor Lookout". We'd like the tagline to read - "There's nothing healthy about driving an hour to see your doctor. So we're coming to you." Opening Late 2025 I have attached three logos as we have two other practices (Harbor Urgent and Harbor Aesthetics ) that should be present on the bottom of the sign but the main business is Harbor Healthcare. For more information on our look/feel visit our website www.wekeepitplain.example (which should be somewhere on the banner as well)
Updates

The signage needs to say Coming Late Fall 2025!

Target Market(s)

Drive By traffic must be made aware that we are coming soon

Industry/Entity Type

Healthcare

Requirements
Nice to have
• Western Theme

```html
<!DOCTYPE html>
<html lang="en">
<head>
<meta charset="utf-8">
<title>Harbor Healthcare – Coming Late Fall 2025 Banner</title>
<link rel="stylesheet" href="https://fonts.googleapis.com/css2?family=Montserrat:wght@400;600;700;800;900&display=swap">
<style>
  :root {
    --sky-blue: #62b0e2;
    --navy: #13325b;
    --white: #ffffff;
    --page: #f2f3f5;
    --urgent-red: #e53935;
    --aesthetic-pink: #e5247a;
  }
  * { margin: 0; padding: 0; box-sizing: border-box; }
  html, body {
    width: 1016px; height: 1200px; overflow: hidden;
    background: var(--page);
    font-family: "Montserrat", Arial, sans-serif;
  }
  .banner {
    position: absolute; left: 28px; top: 361px;
    width: 960px; height: 478px;
    background: var(--white);
    box-shadow: 0 4px 18px rgba(0,0,0,.18);
    overflow: hidden;
  }
  .accent-bar {
    position: absolute; left: 0; top: 21px;
    width: 8px; height: 187px; background: var(--sky-blue);
  }
  .headline {
    position: absolute; left: 20px; top: 12px;
    font-weight: 900; text-transform: uppercase;
    font-size: 110px; line-height: 96px; letter-spacing: -4px;
  }
  .headline .light { color: var(--sky-blue); }
  .headline .dark { color: var(--navy); }
  .brand {
    position: absolute; left: 22px; top: 240px;
    display: flex; align-items: center; gap: 22px;
  }
  .brand-mark {
    width: 92px; height: 92px; background: var(--sky-blue);
    border-radius: 10px;
  }
  .brand-name {
    color: var(--navy); font-weight: 700; text-transform: uppercase;
  }
  .brand-name .line1 { display: block; font-size: 52px; letter-spacing: 12px; line-height: 58px; }
  .brand-name .line2 { display: block; font-size: 30px; letter-spacing: 6.5px; line-height: 38px; }
  .tagline {
    position: absolute; left: 503px; top: 238px;
    width: 457px; height: 103px;
    background: var(--navy); color: var(--white);
    padding: 10px 0 0 13px;
    font-size: 23px; line-height: 28px; font-weight: 400;
    text-transform: uppercase; letter-spacing: .3px;
  }
  .tagline b { font-weight: 800; }
  .tagline .accent { color: var(--sky-blue); font-weight: 800; }
  .sister {
    position: absolute; top: 352px;
    display: flex; align-items: center; gap: 10px;
    color: var(--navy); font-weight: 700; text-transform: uppercase;
    font-size: 17px; line-height: 20px; letter-spacing: 3px;
  }
  .sister.urgent { left: 520px; }
  .sister.aesthetics { left: 752px; }
  .sister .dot { width: 38px; height: 38px; flex: none; }
  .sister.urgent .dot { background: var(--urgent-red); border-radius: 4px; }
  .sister.aesthetics .dot { background: var(--aesthetic-pink); border-radius: 50%; }
  .contact {
    position: absolute; top: 408px; height: 70px;
    display: flex; align-items: center; color: var(--white); font-weight: 700;
  }
  .contact.phone { left: 0; width: 463px; background: var(--sky-blue); padding-left: 22px; gap: 10px; font-size: 40px; }
  .contact.web { left: 470px; width: 490px; background: var(--navy); padding-left: 24px; gap: 12px; font-size: 26px; letter-spacing: -.3px; }
  .contact svg { flex: none; }
  .contact.web .domain { color: var(--sky-blue); }
</style>
</head>
<body>
  <section class="banner">
    <div class="accent-bar"></div>
    <h1 class="headline">
      <span class="light">Coming</span> <span class="dark">Late</span><br>
      <span class="dark">Fall</span> <span class="light">2025!</span>
    </h1>

    <div class="brand">
      <div class="brand-mark"></div>
      <div class="brand-name"><span class="line1">Harbor</span><span class="line2">Healthcare</span></div>
    </div>

    <p class="tagline">
      Conserving <b>Rural John’s<br>Island</b> with home grown<br>progressive <span class="accent">primary care</span>
    </p>

    <div class="sister urgent"><span class="dot"></span><span>Harbor<br>Urgent</span></div>
    <div class="sister aesthetics"><span class="dot"></span><span>Harbor<br>Aesthetics</span></div>

    <div class="contact phone">
      <svg width="38" height="38" viewBox="0 0 38 38" aria-hidden="true">
        <circle cx="19" cy="19" r="19" fill="#fff"/>
        <path d="M13 10c1-1 2-1 3 0l2 3c.6 1 .4 2-.4 2.7l-1.2 1c.9 2 2.6 3.8 4.6 4.8l1-1.2c.7-.8 1.8-1 2.7-.4l3 2c1 .8 1 2 0 3l-1.5 1.5c-1.4 1.3-4 1-7-1-3-2-5.6-4.8-7.3-7.8-1.5-2.8-1.7-5.3-.4-6.6z" fill="var(--sky-blue)"/>
      </svg>
      <span>(555) 014-2290</span>
    </div>

    <div class="contact web">
      <svg width="38" height="38" viewBox="0 0 38 38" aria-hidden="true">
        <circle cx="19" cy="19" r="19" fill="var(--sky-blue)"/>
        <g fill="none" stroke="var(--navy)" stroke-width="1.6">
          <circle cx="19" cy="19" r="10"/>
          <ellipse cx="19" cy="19" rx="4.5" ry="10"/>
          <line x1="9" y1="19" x2="29" y2="19"/>
          <line x1="11" y1="14" x2="27" y2="14"/>
          <line x1="11" y1="24" x2="27" y2="24"/>
        </g>
      </svg>
      <span>www.<span class="domain">wekeepitplain</span>.example</span>
    </div>
  </section>
</body>
</html>
```